Health care technology software systems

We have a solid logo. We have company colors that will need to be used as well. We just need a great business card design. We sell to health plans but want to be modern
Updates

Need extra days to review

Target Market(s)

Health technology sector selling into Health Plans

Industry/Entity Type

Health Care Technology

Contact Information for Business Card

Name, title, address, phone number, email

Requirements
Must have
• Use of Kembrata corporate colors - Uploaded w/ our logos

```html
<!DOCTYPE html>
<html lang="en">
<head>
<meta charset="utf-8">
<title>Kembrata Business Card</title>
<link rel="stylesheet" href="https://fonts.googleapis.com/css2?family=Montserrat:wght@400;500;700&family=Raleway:wght@400&display=swap">
<style>
  :root {
    --page: #ffffff;
    --card: #ffffff;
    --ink: #3b3e4f;
    --navy: #3a4f9c;
    --rule: #24478f;
    --sky: #29a8e0;
    --leaf: #8dc63f;
    --soft-sky: #c4e5f4;
    --soft-leaf: #dfeec9;
    --soft-navy: #c6cde3;
  }
  * { margin: 0; padding: 0; box-sizing: border-box; }
  html, body {
    width: 1200px; height: 2256px; overflow: hidden;
    background: var(--page);
    font-family: "Montserrat", sans-serif;
  }
  .card {
    position: absolute; left: 214px;
    width: 773px; height: 442px;
    background: var(--card);
    overflow: hidden;
    box-shadow: 0 6px 26px rgba(0,0,0,0.22);
  }
  .card--front { top: 1135px; }
  .card--back { top: 1652px; }

  .brand {
    position: absolute; display: flex; align-items: center; gap: 26px;
  }
  .brand__dot {
    width: 62px; height: 62px; border-radius: 50%; background: var(--sky);
  }
  .brand__name {
    font-family: "Raleway", sans-serif; font-weight: 400;
    font-size: 62px; line-height: 1; color: var(--ink);
  }
  .card--front .brand { left: 343px; top: 195px; }
  .card--back .brand { left: 372px; top: 117px; }
  .card--back .brand__dot { width: 56px; height: 56px; }
  .card--back .brand__name { font-size: 58px; }

  .backdrop-mark {
    position: absolute; left: -4px; top: 35px;
    width: 298px; height: 334px; border-radius: 50%;
    background: linear-gradient(135deg, var(--soft-leaf) 0%, var(--soft-sky) 55%, var(--soft-navy) 100%);
    opacity: 0.8;
  }
  .web-front {
    position: absolute; left: 415px; top: 316px;
    font-size: 20px; font-weight: 500; letter-spacing: 3px; color: var(--ink);
  }
  .web-front span { color: var(--navy); }

  .band { position: absolute; bottom: 0; }
  .band--leaf { background: var(--leaf); }
  .band--navy { background: var(--navy); }
  .band--sky { background: var(--sky); }
  .card--front .band--leaf { left: 0; width: 356px; height: 26px; border-top-right-radius: 14px; }
  .card--front .band--navy { left: 363px; right: 0; height: 13px; }
  .card--back .band--sky { left: 0; width: 419px; height: 14px; }
  .card--back .band--leaf { left: 426px; right: 0; height: 28px; border-top-left-radius: 14px; }

  .rule {
    position: absolute; left: 46px; width: 671px; top: 220px;
    height: 2px; background: var(--rule);
  }
  .identity { position: absolute; left: 43px; top: 238px; }
  .identity__company { font-size: 33px; font-weight: 700; color: var(--ink); line-height: 1.1; }
  .identity__role { font-size: 21px; font-weight: 400; color: var(--navy); margin-top: 4px; word-spacing: 3px; }

  .contacts { position: absolute; list-style: none; }
  .contacts li {
    display: flex; align-items: center; gap: 14px;
    font-size: 15px; font-weight: 500; color: var(--ink);
    height: 28px;
  }
  .contacts svg { width: 20px; height: 20px; fill: var(--navy); flex: none; }
  .contacts--phone { left: 44px; top: 318px; }
  .contacts--web { left: 540px; top: 326px; }
  .contacts--web li { gap: 18px; }
</style>
</head>
<body>

<section class="card card--front">
  <div class="backdrop-mark" role="img" aria-label="Large faint brand emblem"></div>
  <div class="brand">
    <span class="brand__dot"></span>
    <span class="brand__name">Kembrata</span>
  </div>
  <p class="web-front">www.<span>kembrata</span>.com</p>
  <div class="band band--leaf"></div>
  <div class="band band--navy"></div>
</section>

<section class="card card--back">
  <div class="brand">
    <span class="brand__dot"></span>
    <span class="brand__name">Kembrata</span>
  </div>
  <div class="rule"></div>
  <div class="identity">
    <h1 class="identity__company">Kembrata LLC</h1>
    <p class="identity__role">Medicare Stars Consulting</p>
  </div>
  <ul class="contacts contacts--phone">
    <li>
      <svg viewBox="0 0 24 24" aria-hidden="true"><path d="M2 9c0-3 4-5 10-5s10 2 10 5v2h-5V8.5c-1.5-.6-3.2-.9-5-.9s-3.5.3-5 .9V11H2zM6 12h12l2 8H4z"/></svg>
      555-218-4630
    </li>
    <li>
      <svg viewBox="0 0 24 24" aria-hidden="true"><circle cx="12" cy="12" r="11"/><path d="M8.5 6.5l2 3-1.2 1.3c.8 1.7 2 2.9 3.6 3.7l1.3-1.2 3 2-1.4 2.2c-4.6-.5-8.5-4.4-9-9z" fill="#fff"/></svg>
      555-218-4631
    </li>
  </ul>
  <ul class="contacts contacts--web">
    <li>
      <svg viewBox="0 0 24 24" aria-hidden="true"><path d="M3 7h18v13H3z"/><path d="M3 7l9 7 9-7" fill="none" stroke="#fff" stroke-width="1.6"/></svg>
      info@kembrata.com
    </li>
    <li>
      <svg viewBox="0 0 24 24" aria-hidden="true"><circle cx="12" cy="12" r="10"/><path d="M2 12h20M12 2c3 3 3 17 0 20M12 2c-3 3-3 17 0 20" fill="none" stroke="#fff" stroke-width="1.4"/></svg>
      www.kembrata.com
    </li>
  </ul>
  <div class="band band--sky"></div>
  <div class="band band--leaf"></div>
</section>

</body>
</html>
```